Box Design for Flooring product

***IMPORTANT: PLEASE READ THE DOCUMENT PROVIDED WITH THIS BRIEF CAREFULLY BEFORE ACCEPTING THIS PROJECT***
Need a creative design for the packaging of a flooring product. The packaging is two boxes: one holding 36 planks of flooring, and the other 7 planks of flooring. There are 4 colours for the flooring planks that need a box designed (for both the 36 plank box and 7 plank box). The boxes measures 92 cm x 16cm x 7cm (36 planks) and 92 cm x 16cm x 1.5cm (7 planks).
More details are provided in the requirements document attached with this brief. Also attaching other supporting documents with this brief mentioned in the document.
Need extra days to review
- Montserrat-Regular

```html
<!DOCTYPE html>
<html lang="en">
<head>
<meta charset="utf-8">
<title>Veridane Self Adhesive Vinyl Planks – 36 Planks Box</title>
<link rel="stylesheet" href="https://fonts.googleapis.com/css2?family=Montserrat:wght@400;500;600;700&display=swap">
<style>
  :root {
    --olive: #4a4734;
    --olive-dark: #3f3c2c;
    --tan: #efc97f;
    --tan-light: #f3d394;
    --paper: #ffffff;
    --ink: #2b2a22;
    --wood-1: #d9a45a;
    --wood-2: #b97c35;
    --wall: #c9d3cc;
  }
  html, body {
    margin: 0;
    padding: 0;
    width: 1200px;
    height: 1000px;
    overflow: hidden;
    background: #ffffff;
  }
  .dieline {
    display: block;
    width: 1200px;
    height: 1000px;
    font-family: "Montserrat", sans-serif;
  }
  .brand-name { font-weight: 500; fill: var(--paper); letter-spacing: 0.5px; }
  .brand-tag { font-weight: 500; fill: var(--paper); letter-spacing: 2.2px; }
  .headline { font-weight: 700; fill: var(--paper); }
  .subline { font-weight: 400; fill: var(--paper); }
  .dark-text { fill: var(--olive); }
  .info-text { font-weight: 500; fill: var(--olive); }
  .step-title { font-weight: 700; fill: var(--ink); font-size: 3.6px; }
  .step-body { font-weight: 400; fill: #555; font-size: 3.2px; }
  .icon-label { font-weight: 400; fill: #d8d4c4; font-size: 5.5px; }
  .table-text { font-weight: 600; fill: var(--ink); font-size: 4.6px; }
</style>
</head>
<body>
<svg class="dieline" viewBox="58 -168 1300 1083" xmlns="http://www.w3.org/2000/svg" aria-label="Flat box dieline for Veridane self adhesive vinyl planks, 36 planks, natural oak">
  <defs>
    <clipPath id="box-outline">
      <polygon points="190,60 1230,60 1254,143 162,143"/>
      <rect x="162" y="143" width="1092" height="544"/>
      <polygon points="82,147 162,143 162,333 82,329"/>
      <polygon points="82,340 162,337 162,410 82,407"/>
      <polygon points="82,422 162,417 162,603 82,598"/>
      <polygon points="82,612 162,607 162,687 82,683"/>
      <polygon points="1254,143 1334,147 1334,329 1254,333"/>
      <polygon points="1254,337 1334,340 1334,407 1254,410"/>
      <polygon points="1254,417 1334,422 1334,598 1254,603"/>
      <polygon points="1254,607 1334,612 1334,683 1254,687"/>
    </clipPath>
    <linearGradient id="room-photo" x1="0" y1="0" x2="0" y2="1">
      <stop offset="0" stop-color="var(--wall)"/>
      <stop offset="0.45" stop-color="#dfe3dc"/>
      <stop offset="0.5" stop-color="var(--wood-1)"/>
      <stop offset="1" stop-color="var(--wood-2)"/>
    </linearGradient>
    <linearGradient id="oak-swatch" x1="0" y1="0" x2="1" y2="1">
      <stop offset="0" stop-color="#e2b064"/>
      <stop offset="1" stop-color="#c88c40"/>
    </linearGradient>
  </defs>

  <!-- Box artwork -->
  <g clip-path="url(#box-outline)">
    <rect class="base" x="80" y="58" width="1260" height="632" fill="var(--olive)"/>
    <!-- diagonal stripes and tan field -->
    <polygon points="1000,60 1012,60 705,687 693,687" fill="var(--tan-light)"/>
    <polygon points="1022,60 1034,60 727,687 715,687" fill="var(--tan-light)"/>
    <polygon points="1045,60 1340,60 1340,690 738,690" fill="var(--tan)"/>
    <!-- dark wedge -->
    <polygon points="738,687 975,687 870,445" fill="var(--olive)"/>
    <polygon points="858,475 910,585 802,585" fill="var(--paper)"/>
    <!-- room photo area -->
    <polygon points="895,413 1062,413 1062,603 935,603" fill="url(#room-photo)" role="img" aria-label="Photo of a bright room with natural oak vinyl plank flooring"/>
  </g>

  <!-- panel folds -->
  <g class="fold-lines" stroke="#ffffff" stroke-opacity="0.9" stroke-width="2">
    <line x1="82" y1="335" x2="162" y2="335"/>
    <line x1="82" y1="414" x2="162" y2="414"/>
    <line x1="82" y1="605" x2="162" y2="605"/>
    <line x1="1254" y1="335" x2="1334" y2="335"/>
    <line x1="1254" y1="414" x2="1334" y2="414"/>
    <line x1="1254" y1="605" x2="1334" y2="605"/>
  </g>

  <!-- ===== Back panel ===== -->
  <g class="brand-lockup">
    <rect x="190" y="164" width="28" height="28" fill="var(--paper)"/>
    <text class="brand-name" x="226" y="188" font-size="25">VERIDANE</text>
    <text class="brand-tag" x="227" y="197" font-size="6.4">PREMIUM FLOORS AND TILES</text>
  </g>
  <text class="headline" x="190" y="266" font-size="24">SELF ADHESIVE</text>
  <text class="headline" x="190" y="292" font-size="24">VINYL PLANKS</text>
  <text class="subline" x="190" y="312" font-size="12.5">Suitable for general domestic use</text>

  <g class="install-card">
    <rect x="472" y="156" width="392" height="165" rx="4" fill="var(--paper)"/>
    <text x="478" y="165" font-size="4.6" font-weight="700" fill="var(--ink)">Installation instructions</text>
    <!-- column 1 -->
    <text class="step-title" x="478" y="172">Step 1 : Tools Needed</text>
    <rect x="478" y="175" width="22" height="22" fill="#d9b07a" role="img" aria-label="Tools for installation"/>
    <text class="step-body" x="504" y="180">Utility knife, ruler, pencil and cloth.</text>
    <text class="step-title" x="478" y="205">Step 2 : Acclimatize your floor</text>
    <rect x="478" y="208" width="22" height="22" fill="#cfc7b2" role="img" aria-label="Stacked plank boxes"/>
    <text class="step-body" x="504" y="213">Store boxes in room for 24h.</text>
    <text class="step-title" x="478" y="257">Step 3 : Removing Skirting board</text>
    <rect x="478" y="260" width="22" height="22" fill="#bdb6a2" role="img" aria-label="Removing skirting board"/>
    <text class="step-body" x="504" y="265">Carefully remove skirting boards from all walls.</text>
    <text class="step-title" x="478" y="290">Step 4 : Planning your remove</text>
    <rect x="478" y="293" width="22" height="22" fill="#d6c29a" role="img" aria-label="Planning the layout"/>
    <text class="step-body" x="504" y="298">Remove old flooring and level the base.</text>
    <!-- column 2 -->
    <text class="step-title" x="608" y="172">Step 5 : Get ready to lay</text>
    <rect x="608" y="175" width="22" height="22" fill="#c9b48e" role="img" aria-label="Preparing the floor"/>
    <text class="step-body" x="634" y="180">Clean and dry the floor before laying.</text>
    <text class="step-title" x="608" y="205">Step 6 : Dry lay your planks</text>
    <rect x="608" y="208" width="22" height="22" fill="#a9b3a8" role="img" aria-label="Dry laying planks"/>
    <text class="step-body" x="634" y="213">Lay planks loosely to check the pattern.</text>
    <text class="step-title" x="608" y="257">Step 7 : Arrows on the backing paper</text>
    <rect x="608" y="260" width="22" height="22" fill="#c3bba5" role="img" aria-label="Arrows on backing paper"/>
    <text class="step-body" x="634" y="265">Follow arrows on paper for same direction.</text>
    <text class="step-title" x="608" y="290">Step 8 : Laying the first plank</text>
    <rect x="608" y="293" width="22" height="22" fill="#d4c6a6" role="img" aria-label="Laying the first plank"/>
    <text class="step-body" x="634" y="298">Peel backing and press first plank firmly.</text>
    <!-- column 3 -->
    <text class="step-title" x="738" y="172">Step 9 : Laying the remaining planks</text>
    <rect x="738" y="175" width="22" height="22" fill="#a8b2a0" role="img" aria-label="Laying remaining planks"/>
    <text class="step-body" x="764" y="180">Continue row by row, staggering the joints.</text>
    <text class="step-title" x="738" y="205">Step 10 : Cutting the planks</text>
    <rect x="738" y="208" width="22" height="22" fill="#c2a77e" role="img" aria-label="Cutting a plank"/>
    <text class="step-body" x="764" y="213">Measure and score the plank with knife.</text>
    <text class="step-title" x="738" y="257">Step 11 : Breaking the cut plank</text>
    <rect x="738" y="260" width="22" height="22" fill="#9fa699" role="img" aria-label="Breaking the cut plank"/>
    <text class="step-body" x="764" y="265">Bend the plank to snap along cut.</text>
    <text class="step-title" x="738" y="290">Step 12 : Laying the cut planks</text>
    <rect x="738" y="293" width="22" height="22" fill="#b4ad98" role="img" aria-label="Laying cut planks"/>
    <text class="step-body" x="764" y="298">Lay cut pieces and press edges down.</text>
  </g>

  <g class="producer-info" text-anchor="end" font-size="6.4">
    <text class="info-text" x="1108" y="166" font-weight="700">Produced by :</text>
    <text class="info-text" x="1108" y="174">Veridane</text>
    <text class="info-text" x="1108" y="182">14 Larch Road, Unit 3</text>
    <text class="info-text" x="1108" y="190">Millbrook, 40210</text>
    <text class="info-text" x="1108" y="198">www.veridanefloors.com</text>
    <text class="info-text" x="1108" y="206" font-weight="700">Customer Service :</text>
    <text class="info-text" x="1108" y="214">555-014-2290</text>
  </g>

  <g class="compliance-table">
    <rect x="1001" y="226" width="107" height="89" fill="var(--paper)" stroke="var(--ink)" stroke-width="1.2"/>
    <rect x="1038" y="232" width="32" height="28" rx="2" fill="var(--ink)"/>
    <text class="table-text" x="1054" y="268" text-anchor="middle">Veridane Premium Floors and Tiles</text>
    <line x1="1001" y1="279" x2="1108" y2="279" stroke="var(--ink)" stroke-width="0.8"/>
    <text class="table-text" x="1004" y="285" font-size="4">EN 14041, EN 13501-1, EN 717-1, EN 13893</text>
    <line x1="1001" y1="288" x2="1108" y2="288" stroke="var(--ink)" stroke-width="0.8"/>
    <text class="table-text" x="1004" y="294">Reaction to Fire</text>
    <text class="table-text" x="1100" y="294" text-anchor="end">Bfl-s1</text>
    <line x1="1001" y1="297" x2="1108" y2="297" stroke="var(--ink)" stroke-width="0.8"/>
    <text class="table-text" x="1004" y="303">Emission of Formaldehyde</text>
    <text class="table-text" x="1100" y="303" text-anchor="end">E1</text>
    <line x1="1001" y1="306" x2="1108" y2="306" stroke="var(--ink)" stroke-width="0.8"/>
    <text class="table-text" x="1004" y="312">Slipperiness</text>
    <text class="table-text" x="1100" y="312" text-anchor="end">DS</text>
  </g>

  <g class="pack-info-small">
    <rect x="1118" y="162" width="133" height="30" fill="var(--olive)"/>
    <text x="1155" y="187" font-size="22" font-weight="700" fill="var(--tan)">36</text>
    <text x="1190" y="187" font-size="11" font-weight="600" fill="var(--tan)">Planks</text>
    <text class="info-text" x="1116" y="205" font-size="10.5" font-weight="700">Pack coverage 5 m²</text>
    <rect x="1125" y="210" width="100" height="44" fill="none" stroke="var(--olive)" stroke-width="1.5"/>
    <text class="info-text" x="1221" y="221" font-size="7.6" text-anchor="end">Plank Size :</text>
    <text class="info-text" x="1221" y="231" font-size="7.6" text-anchor="end">914 mm x 152 mm</text>
    <text class="info-text" x="1221" y="239" font-size="5.4" text-anchor="end">(36" x 6" approx.)</text>
    <text class="info-text" x="1221" y="249" font-size="7.6" text-anchor="end">1.8 mm (0.07") Thickness</text>
  </g>

  <!-- ===== Upside-down side panel ===== -->
  <g transform="rotate(180 500 375)">
    <text class="headline" x="500" y="387" font-size="30" text-anchor="middle" letter-spacing="1">SELF ADHESIVE VINYL PLANKS</text>
  </g>
  <g transform="rotate(180 1125 373)">
    <rect x="1030" y="358" width="28" height="28" fill="var(--olive)"/>
    <text x="1066" y="382" font-size="25" font-weight="500" fill="var(--olive)">VERIDANE</text>
    <text x="1067" y="391" font-size="6.4" font-weight="500" letter-spacing="2.2" fill="var(--olive)">PREMIUM FLOORS AND TILES</text>
  </g>

  <!-- ===== Front panel ===== -->
  <g class="brand-lockup">
    <rect x="190" y="434" width="28" height="28" fill="var(--paper)"/>
    <text class="brand-name" x="226" y="458" font-size="25">VERIDANE</text>
    <text class="brand-tag" x="227" y="467" font-size="6.4">PREMIUM FLOORS AND TILES</text>
  </g>

  <g class="feature-icons">
    <rect x="590" y="433" width="52" height="52" rx="4" fill="#c9c4ad" stroke="#e8e4d2" stroke-width="2" role="img" aria-label="Illustration of a plank being laid"/>
    <text class="icon-label" x="616" y="494" text-anchor="middle">Easy to lay</text>
    <rect x="653" y="433" width="52" height="52" rx="4" fill="#5fb7c9" stroke="#e8e4d2" stroke-width="2" role="img" aria-label="Illustration of cleaning a wet floor"/>
    <text class="icon-label" x="679" y="494" text-anchor="middle">Water resistant,</text>
    <text class="icon-label" x="679" y="501" text-anchor="middle">easy to clean</text>
    <rect x="716" y="433" width="52" height="52" rx="4" fill="#e9d56a" stroke="#e8e4d2" stroke-width="2" role="img" aria-label="Illustration of bathroom and kitchen use"/>
    <text class="icon-label" x="742" y="494" text-anchor="middle">Ideal for Bathrooms</text>
    <text class="icon-label" x="742" y="501" text-anchor="middle">and Kitchens</text>
  </g>

  <text class="headline" x="190" y="559" font-size="30.5" letter-spacing="0.5">SELF ADHESIVE VINYL PLANKS</text>
  <text class="subline" x="190" y="583" font-size="14">Suitable for general domestic use</text>

  <g class="pack-info-front">
    <rect x="1068" y="433" width="183" height="31" fill="var(--olive)"/>
    <text x="1133" y="459" font-size="25" font-weight="700" fill="var(--tan)">36</text>
    <text x="1173" y="459" font-size="14" font-weight="600" fill="var(--tan)">Planks</text>
    <text class="info-text" x="1073" y="482" font-size="13.5" font-weight="700">Pack coverage 5 m²</text>
    <rect x="1068" y="490" width="157" height="55" fill="none" stroke="var(--olive)" stroke-width="1.5"/>
    <text class="info-text" x="1221" y="505" font-size="11" text-anchor="end">Plank Size :</text>
    <text class="info-text" x="1221" y="518" font-size="11" text-anchor="end">914 mm x 152 mm</text>
    <text class="info-text" x="1221" y="528" font-size="8" text-anchor="end">(36" x 6" approx.)</text>
    <text class="info-text" x="1221" y="541" font-size="11" text-anchor="end">1.8 mm (0.07") Thickness</text>
    <rect x="1039" y="554" width="198" height="38" rx="6" fill="url(#oak-swatch)" stroke="var(--olive)" stroke-width="4" role="img" aria-label="Natural oak wood grain swatch"/>
    <text x="1046" y="582" font-size="14" font-weight="500" fill="var(--olive)">NATURAL OAK</text>
  </g>

  <g transform="rotate(-90 1294 510)">
    <text x="1294" y="500" font-size="24" font-weight="700" fill="var(--olive)" text-anchor="middle">36 <tspan font-size="14" font-weight="600">Planks</tspan></text>
    <text x="1294" y="518" font-size="12" font-weight="500" fill="var(--olive)" text-anchor="middle">NATURAL OAK</text>
  </g>

  <g transform="rotate(90 121 510)">
    <rect x="64" y="506" width="12" height="12" fill="var(--paper)"/>
    <text class="brand-name" x="81" y="516" font-size="11">VERIDANE</text>
    <text class="brand-tag" x="81" y="521" font-size="3" letter-spacing="1">PREMIUM FLOORS AND TILES</text>
  </g>

  <!-- ===== Bottom side panel ===== -->
  <g class="brand-lockup">
    <rect x="190" y="628" width="28" height="28" fill="var(--paper)"/>
    <text class="brand-name" x="226" y="652" font-size="25">VERIDANE</text>
    <text class="brand-tag" x="227" y="661" font-size="6.4">PREMIUM FLOORS AND TILES</text>
  </g>
  <text x="856" y="648" font-size="25" font-weight="700" fill="var(--paper)" text-anchor="middle">36 <tspan font-size="14" font-weight="600">Planks</tspan></text>
  <text class="subline" x="856" y="666" font-size="13.5" text-anchor="middle">NATURAL OAK</text>
</svg>
</body>
</html>
```